Plinthmoor Assessments Landing Page

We need a landing page re-designed for a new website www.plinthmoorassessments.example and the website is live if you search the address provided.
We need the industry standard files for embedding this into the landing page of our website. The company is a real estate advisory firm, we provide professional property services and are focused on business rates (commercial property taxation in the UK).
We have uploaded a file which is meant to provide a visual guide as to how we envisage the landing page looking. You are free to come up with an entirely different creative design. The image at the top with the search button is taken from another website so the design will need to be distinctly different but may follow the same theme. Furthermore, the colour palette does not need to be followed slavishly and can be modified changed and improved upon. It might be that you want to incorporate other visual cues such as a desktop PC, laptop and iPad as these are devices the website will be accessed from; however, this is not essential and only a guide.
**To clarify, please note, the target industry is commercial properties and not residential or domestic property, so please when incorporating designs of buildings its important to focus on commercial property such as shops, offices, industrial buildings etc.**
Target Market(s)
Occupiers of commercial real estate in the UK who pay property tax to occupy the property.
Look and feel
Each slider illustrates characteristics of the customer's brand and the style your logo design should communicate.

```html
<!DOCTYPE html>
<html lang="en">
<head>
<meta charset="utf-8">
<title>Plinthmoor Assessments</title>
<link href="https://fonts.googleapis.com/css2?family=Raleway:wght@700;800;900&family=Roboto:wght@400;500;700&display=swap" rel="stylesheet">
<style>
:root{
  --orange:#f07a22;
  --orange-dark:#e8661a;
  --navy:#0d2a5c;
  --navy-deep:#0a2150;
  --ink:#2b2b2b;
  --muted:#8a8a8a;
  --line:#e2e2e2;
  --white:#ffffff;
  --ghost:rgba(0,0,0,0.06);
}
*{box-sizing:border-box;margin:0;padding:0}
html,body{width:1200px;height:4688px;overflow:hidden}
body{position:relative;background:var(--white);font-family:'Roboto',Arial,sans-serif;color:var(--ink)}
.abs{position:absolute}
.heading{font-family:'Raleway',Arial,sans-serif;font-weight:800;color:var(--ink)}
.btn{position:absolute;display:flex;align-items:center;justify-content:center;background:var(--orange);color:#fff;font-family:'Raleway',Arial,sans-serif;font-weight:800;font-size:15px;text-transform:uppercase;gap:6px}
.btn .dot{width:12px;height:12px;border-radius:50%;background:#fff;display:inline-block;position:relative}
.btn .dot::after{content:"";position:absolute;left:4px;top:3px;border-left:5px solid var(--orange);border-top:3px solid transparent;border-bottom:3px solid transparent}
.btn.navy{background:var(--navy)}
.btn.navy .dot::after{border-left-color:var(--navy)}
.para{font-size:13.5px;line-height:24px;color:var(--muted);text-align:justify}

/* top bar */
.topbar{left:0;top:0;width:1200px;height:36px;background:var(--navy);color:#fff;font-size:12px}
.topbar .addr{position:absolute;left:142px;top:11px}
.topbar .follow{position:absolute;right:142px;top:11px;display:flex;gap:10px}
.header{left:0;top:36px;width:1200px;height:95px;background:#fff}
.brand{position:absolute;left:142px;top:26px;display:flex;align-items:center;gap:10px;font-family:'Raleway',sans-serif;font-weight:800;font-size:17px;line-height:20px;color:var(--ink)}
.brand .sq{width:30px;height:30px;background:var(--orange)}
.nav{position:absolute;left:447px;top:38px;display:flex;gap:32px;font-family:'Raleway',sans-serif;font-weight:800;font-size:14px;color:var(--ink)}
.nav-cta{left:887px;top:28px;width:168px;height:40px;font-size:14px}

/* hero */
.hero-title{left:0;top:296px;width:1200px;text-align:center;color:#fff;font-size:43px;line-height:48px;text-shadow:0 2px 6px rgba(0,0,0,.5)}
.hero-sub{left:0;top:420px;width:1200px;text-align:center;color:#fff;font-size:15px;font-weight:500;line-height:27px;text-shadow:0 1px 4px rgba(0,0,0,.6)}
.search{left:220px;top:495px;width:760px;height:48px;display:flex}
.search .field{flex:1;background:#fff;color:var(--muted);font-size:12px;padding:17px 18px}
.search .go{width:182px;background:var(--orange);color:#fff;font-family:'Raleway',sans-serif;font-weight:800;font-size:15px;display:flex;align-items:center;justify-content:center}

/* about */
.side-word{font-family:'Raleway',sans-serif;font-weight:900;color:var(--ghost);font-size:80px;white-space:nowrap}
.about-kicker{left:142px;top:866px;font-size:40px;color:var(--orange)}
.about-title{left:142px;top:918px;font-size:31px;white-space:nowrap;width:460px}
.about-text{left:142px;top:982px;width:455px}
.photo{position:absolute}
.divider{position:absolute;left:142px;width:912px;height:1px;background:var(--line)}

/* section titles with ghost words */
.sec{left:0;width:1200px;text-align:center}
.sec .ghost{position:absolute;left:0;width:1200px;text-align:center;font-family:'Raleway',sans-serif;font-weight:900;font-size:76px;color:rgba(0,0,0,0.06);top:-18px}
.sec .title{position:relative;font-family:'Raleway',sans-serif;font-weight:800;font-size:40px;color:var(--ink)}

.card{position:absolute;top:1495px;width:282px;height:299px;background:#fff;border:1px solid #ececec;box-shadow:0 2px 8px rgba(0,0,0,.06);text-align:center}
.card.active{border-top:3px solid var(--navy)}
.card .icon{width:92px;height:92px;border-radius:50%;margin:26px auto 0;background:var(--navy);display:flex;align-items:center;justify-content:center}
.card .icon.or{background:var(--orange)}
.card h3{font-family:'Raleway',sans-serif;font-weight:800;font-size:17px;margin-top:28px;color:var(--ink)}
.card p{font-size:12.5px;line-height:23px;color:var(--muted);margin:12px 18px 0}
.card .more{display:inline-block;margin-top:10px;color:var(--orange);font-size:13.5px;font-weight:700;text-decoration:underline}

/* estimate */
.est-title{left:0;top:2735px;width:1200px;text-align:center;color:#fff;font-size:40px;font-family:'Raleway',sans-serif;font-weight:800}
.est-ghost{left:0;top:2718px;width:1200px;text-align:center;color:rgba(255,255,255,0.1);font-size:76px;font-family:'Raleway',sans-serif;font-weight:900}
.est-text{left:240px;top:2798px;width:720px;text-align:center;color:#fff;font-size:13.5px;line-height:27px}

/* fees */
.fees-title{left:617px;top:3160px;font-size:40px;line-height:56px;width:560px}

/* reviews */
.review{position:absolute;top:3886px;width:377px;height:233px;background:#fff;box-shadow:0 2px 10px rgba(0,0,0,.1);padding:28px 32px}
.review.faded{opacity:.35}
.review .co{font-family:'Raleway',sans-serif;font-weight:800;font-size:16px;color:var(--ink)}
.review .score{position:absolute;right:32px;top:28px;background:#5b6470;color:#fff;font-size:12px;padding:2px 7px}
.review .stars{position:absolute;right:32px;top:52px;color:var(--orange);font-size:16px;letter-spacing:2px}
.review p{margin-top:34px;font-size:13px;line-height:24px;font-style:italic;color:var(--muted);text-align:justify}
.review p span{color:var(--navy);text-decoration:underline;font-weight:500}
.review .who{margin-top:14px;font-size:13px;font-weight:700;color:#555}

/* footer */
.foot-col{position:absolute;top:4364px;color:#fff}
.foot-col h4{font-family:'Raleway',sans-serif;font-weight:800;font-size:15px;margin-bottom:20px}
.foot-col li{list-style:none;font-size:11.5px;line-height:25px}
.foot-col li::before{content:"»";margin-right:14px}
.contact li::before{content:none}
.contact li{display:flex;gap:14px;margin-bottom:10px;line-height:18px}
.news p{font-size:11.5px;line-height:18px;width:240px}
.news .mail{margin-top:14px;width:236px;height:30px;border:1px solid rgba(255,255,255,.6);font-size:11px;padding:8px 10px}
.news .sub{margin-top:14px;width:100px;height:32px;background:var(--orange);font-family:'Raleway',sans-serif;font-weight:800;font-size:11px;display:flex;align-items:center;justify-content:center}
.social{left:0;top:4571px;width:1200px;display:flex;justify-content:center;gap:10px}
.social span{width:34px;height:34px;border:2px solid #fff;border-radius:50%}
.copy{left:0;top:4640px;width:1200px;text-align:center;color:#fff;font-size:12px}
</style>
</head>
<body>

<!-- top bar & header -->
<div class="abs topbar">
  <div class="addr">⚲ Ferrow House, Quayside Park, Harlbridge HB4 7QT</div>
  <div class="follow"><span>Follow Us On:</span><span>FB</span><span>TW</span><span>IG</span><span>IN</span></div>
</div>
<div class="abs header">
  <div class="brand"><span class="sq"></span><span>PLINTHMOOR<br>ASSESSMENTS</span></div>
  <div class="nav"><span>HOME</span><span>PROPERTY SEARCH</span><span>DISCOVER</span><span>ABOUT</span></div>
  <div class="btn nav-cta">BOOK VALUATION</div>
</div>

<!-- hero shapes -->
<svg class="abs" style="left:0;top:131px" width="1200" height="1060" viewBox="0 131 1200 1060">
  <defs>
    <linearGradient id="heroSky" x1="0" y1="0" x2="0" y2="1">
      <stop offset="0" stop-color="#5d6e8f"/>
      <stop offset="0.35" stop-color="#c77a4c"/>
      <stop offset="0.6" stop-color="#6a5a58"/>
      <stop offset="1" stop-color="#2a3040"/>
    </linearGradient>
  </defs>
  <g role="img" aria-label="Sunset view over a city skyline of office towers">
    <polygon points="0,131 1200,131 1200,700 600,783 0,592" fill="url(#heroSky)"/>
  </g>
  <polygon points="0,592 600,783 0,780" fill="var(--navy)" opacity="0.9"/>
  <polygon points="0,600 600,783 0,783" fill="#fff"/>
  <polygon points="600,783 1200,700 1200,745 1053,1165 1049,1165 1148,760 783,876 1120,790" fill="var(--orange)"/>
  <rect x="585" y="628" width="30" height="48" rx="15" fill="none" stroke="#fff" stroke-width="2.5"/>
  <line x1="600" y1="640" x2="600" y2="652" stroke="#fff" stroke-width="2.5"/>
  <line x1="600" y1="684" x2="600" y2="705" stroke="#fff" stroke-width="2.5"/>
  <polyline points="592,697 600,706 608,697" fill="none" stroke="#fff" stroke-width="2.5"/>
</svg>

<div class="abs heading hero-title">DO YOU THINK YOUR BUSINESS<br>RATES ARE TOO HIGH?</div>
<div class="abs hero-sub">Use our free valuation tool below or book a valuation with one of our qualified surveyors.<br>No shock commissions and fair fixed fees from £295!</div>
<div class="abs search"><div class="field">Enter Your Postcode</div><div class="go">FREE VALUATION</div></div>

<!-- soft background for the middle sections -->
<div class="abs" role="img" aria-label="Faint background of modern office buildings" style="left:0;top:1200px;width:1200px;height:1426px;background:linear-gradient(180deg,#ffffff 0%,#f1efec 40%,#e9e6e2 100%);opacity:.8"></div>

<!-- about -->
<div class="abs side-word" style="left:-112px;top:950px;transform:rotate(-90deg);transform-origin:center;width:300px">ABOUT US</div>
<div class="abs heading about-kicker">ABOUT</div>
<div class="abs heading about-title">PLINTHMOOR ASSESSMENTS</div>
<div class="abs para about-text">Lorem ipsum dolor sit amet, consectetur adipiscing elit, sed do eiusmod tempor incididunt ut labore et dolore magna aliqua. Ut enim ad minim veniam, quis nostrud exercitation ullamco laboris nisi ut aliquip ex ea commodo consequat. Duis aute irure dolor in reprehenderit in voluptate velit esse cillum dolore eu fugiat nulla pariatur.</div>
<div class="btn" style="left:142px;top:1131px;width:154px;height:45px">READ MORE <span class="dot"></span></div>
<div class="photo" role="img" aria-label="Aerial view of a city street with office blocks under blue sky" style="left:646px;top:876px;width:407px;height:299px;border:3px solid #fff;box-shadow:0 3px 10px rgba(0,0,0,.2);background:linear-gradient(180deg,#4f86c4 0%,#a9c4e0 40%,#8e7766 70%,#4b5a48 100%)"></div>

<div class="divider" style="top:1280px"></div>

<!-- services -->
<div class="abs sec" style="top:1362px"><div class="ghost">OUR SERVICES</div><div class="title">OUR SERVICES</div></div>
<div class="abs" style="left:0;top:1432px;width:1200px;text-align:center;font-size:13px;color:var(--muted)">Lorem ipsum dolor sit amet, consectetur adipiscing eiusmod tempor incididunt ut labore et dolore magna aliqua.</div>

<div class="card" style="left:144px">
  <div class="icon"><svg width="46" height="46" viewBox="0 0 46 46" fill="none" stroke="#fff" stroke-width="2"><path d="M4 42V24l10-6v6l10-6v6l10-6v24z"/><path d="M36 42V6h4v36"/></svg></div>
  <h3>INDUSTRIAL BUILDINGS</h3>
  <p>Lorem ipsum dolor amet consec tetur adipiscing sed do eiusmod tempor incididunt do magna aliqua.</p>
  <span class="more">Read More ➜</span>
</div>
<div class="card active" style="left:459px">
  <div class="icon or"><svg width="46" height="46" viewBox="0 0 46 46" fill="none" stroke="#fff" stroke-width="2"><rect x="8" y="6" width="18" height="36"/><rect x="26" y="18" width="12" height="24"/><path d="M12 12h4M18 12h4M12 18h4M18 18h4M12 24h4M18 24h4M12 30h4M18 30h4M30 24h4M30 30h4"/></svg></div>
  <h3>COMMERCIAL PROPERTIES</h3>
  <p>Lorem ipsum dolor amet consec tetur adipiscing sed do eiusmod tempor incididunt do magna aliqua.</p>
  <span class="more">Read More ➜</span>
</div>
<div class="card" style="left:774px">
  <div class="icon"><svg width="46" height="46" viewBox="0 0 46 46" fill="none" stroke="#fff" stroke-width="2"><rect x="4" y="8" width="24" height="16"/><circle cx="32" cy="24" r="6"/><path d="M22 42c0-6 4-10 10-10s10 4 10 10z"/><path d="M8 42h12"/></svg></div>
  <h3>CONSULTING FIRM</h3>
  <p>Lorem ipsum dolor amet consec tetur adipiscing sed do eiusmod tempor incididunt do magna aliqua.</p>
  <span class="more">Read More ➜</span>
</div>

<!-- projects -->
<div class="abs sec" style="top:1894px"><div class="ghost">OUR PROJECTS</div><div class="title">OUR PROJECTS</div></div>
<div class="photo" role="img" aria-label="Glass office buildings at dusk" style="left:146px;top:1998px;width:488px;height:275px;border:3px solid #fff;box-shadow:0 3px 10px rgba(0,0,0,.2);background:linear-gradient(180deg,#3b587c 0%,#8aa3bb 35%,#2f3a47 70%,#6b5a44 100%)"></div>
<div class="photo" role="img" aria-label="Modern industrial warehouse with blue sky" style="left:566px;top:2078px;width:488px;height:277px;border:3px solid #fff;box-shadow:0 3px 10px rgba(0,0,0,.2);background:linear-gradient(180deg,#3f73c2 0%,#8cb0dc 35%,#b6bac0 55%,#8d9096 100%)"></div>
<svg class="abs" style="left:280px;top:2336px" width="160" height="20" viewBox="0 0 160 20">
  <line x1="6" y1="10" x2="24" y2="10" stroke="#999" stroke-width="1.5"/><polyline points="11,6 6,10 11,14" fill="none" stroke="#999" stroke-width="1.5"/>
  <circle cx="42" cy="10" r="4" fill="#ccc"/><circle cx="58" cy="10" r="4" fill="#ccc"/><circle cx="74" cy="10" r="4" fill="var(--orange)"/><circle cx="90" cy="10" r="4" fill="#ccc"/><circle cx="106" cy="10" r="4" fill="#ccc"/>
  <line x1="128" y1="10" x2="146" y2="10" stroke="#999" stroke-width="1.5"/><polyline points="141,6 146,10 141,14" fill="none" stroke="#999" stroke-width="1.5"/>
</svg>
<div class="btn" style="left:483px;top:2431px;width:234px;height:46px">VIEW ALL PROJECTS <span class="dot"></span></div>

<!-- estimate band -->
<svg class="abs" style="left:0;top:2626px" width="1200" height="420" viewBox="0 2626 1200 420">
  <polygon points="0,2626 1200,2626 1200,2932 600,3037 0,2932" fill="var(--orange)"/>
</svg>
<svg class="abs" style="left:0;top:3037px" width="480" height="500" viewBox="0 3037 480 500"><polygon points="0,3037 470,3170 147,3530 0,3530" fill="var(--navy)"/></svg>
<div class="abs est-ghost">GET AN INSTANT ESTIMATE</div>
<div class="abs est-title">GET AN INSTANT ESTIMATE</div>
<div class="abs est-text">Lorem ipsum dolor sit amet, consectetur adipiscing elit, sed do eiusmod tempor incididunt ut labore et dolore magna aliqua. Ut enim ad minim veniam, quis nostrud exercitation ullamco.</div>
<div class="btn navy" style="left:484px;top:2881px;width:226px;height:44px">FREE VALUATION <span class="dot"></span></div>

<!-- fees -->
<div class="abs side-word" style="left:1010px;top:3340px;transform:rotate(90deg);transform-origin:center;width:330px;font-size:72px">FAIR FIXED FEES</div>
<div class="photo" role="img" aria-label="Modern timber-clad commercial block" style="left:147px;top:3170px;width:414px;height:419px;border:3px solid #fff;box-shadow:0 3px 10px rgba(0,0,0,.2);background:linear-gradient(180deg,#dfe6ee 0%,#c8cfd6 30%,#a87c55 60%,#6c6a5c 100%)"></div>
<div class="abs heading fees-title">FAIR FIXED FEES &amp; NO SHOCK COMMISSIONS!</div>
<div class="abs para" style="left:617px;top:3291px;width:437px;line-height:27px">Lorem ipsum dolor sit amet, consectetur adipiscing elit, sed do eiusmod tempor incididunt ut labore et dolore magna aliqua.</div>
<div class="abs para" style="left:617px;top:3371px;width:437px;line-height:27px">Lorem ipsum dolor sit amet, consectetur adipiscing elit, sed do eiusmod tempor incididunt ut labore et dolore magna aliqua. Ut enim ad minim veniam, quis nostrud exercitation ullamco laboris nisi ut aliquip ex ea commodo consequat. Duis aute irure dolor in reprehenderit in voluptate velit esse cillum dolore.</div>
<div class="btn" style="left:617px;top:3547px;width:155px;height:44px">READ MORE <span class="dot"></span></div>

<div class="divider" style="top:3700px"></div>

<!-- reviews -->
<div class="abs sec" style="top:3784px"><div class="ghost">RECENT REVIEWS</div><div class="title">RECENT REVIEWS</div></div>

<div class="review faded" style="left:-204px"><div class="co">Brightmere</div><div class="score">4.5</div><div class="stars">★★★★★</div><p>At vero eos et accusamus et iusto odio dignissimos ducimus qui blanditiis praesentium voluptatum <span>View More</span></p></div>
<div class="review" style="left:206px"><div class="co">Harlow &amp; Kemp</div><div class="score">4.5</div><div class="stars">★★★★★</div><p>At vero eos et accusamus et iusto odio dignissimos ducimus qui blanditiis praesentium voluptatum deleniti atque corrupti dolores... <span>View More</span></p><div class="who">_ Anil Mehta</div></div>
<div class="review" style="left:617px"><div class="co">Ostrava Works</div><div class="score">4.5</div><div class="stars">★★★★★</div><p>At vero eos et accusamus et iusto odio dignissimos ducimus qui blanditiis praesentium voluptatum deleniti atque corrupti dolores... <span>View More</span></p><div class="who">_ Jon Pryce</div></div>
<div class="review faded" style="left:1029px"><div class="co">Corran Stone</div><p>At vero eos et accusamus et iusto odio dignissimos ducimus qui blanditiis deleniti atque corrupti</p><div class="who">_ Tessa Lowe</div></div>
<svg class="abs" style="left:70px;top:3950px" width="40" height="20"><line x1="2" y1="10" x2="36" y2="10" stroke="var(--orange)" stroke-width="2.5"/><polyline points="12,3 2,10 12,17" fill="none" stroke="var(--orange)" stroke-width="2.5"/></svg>
<svg class="abs" style="left:1090px;top:3950px" width="40" height="20"><line x1="2" y1="10" x2="36" y2="10" stroke="var(--orange)" stroke-width="2.5"/><polyline points="26,3 36,10 26,17" fill="none" stroke="var(--orange)" stroke-width="2.5"/></svg>

<!-- footer -->
<svg class="abs" style="left:0;top:4216px" width="1200" height="472" viewBox="0 4216 1200 472">
  <polygon points="0,4370 600,4216 1200,4370 1200,4688 0,4688" fill="var(--orange)"/>
  <polygon points="0,4382 600,4232 1200,4382 1200,4688 0,4688" fill="var(--navy)"/>
  <line x1="600" y1="4250" x2="600" y2="4268" stroke="#fff" stroke-width="2"/>
  <polyline points="593,4257 600,4250 607,4257" fill="none" stroke="#fff" stroke-width="2"/>
  <rect x="588" y="4278" width="24" height="40" rx="12" fill="none" stroke="#fff" stroke-width="2"/>
  <line x1="600" y1="4288" x2="600" y2="4298" stroke="#fff" stroke-width="2"/>
  <line x1="142" y1="4589" x2="505" y2="4589" stroke="rgba(255,255,255,.4)"/>
  <line x1="695" y1="4589" x2="1058" y2="4589" stroke="rgba(255,255,255,.4)"/>
</svg>

<div class="foot-col" style="left:142px"><h4>QUICK LINKS</h4><ul><li>Home</li><li>About Us</li><li>Services</li><li>Our Team</li><li>Contact Us</li></ul></div>
<div class="foot-col" style="left:333px"><h4>OTHER LINKS</h4><ul><li>Careers</li><li>Latest Articles</li><li>Reviews</li><li>FAQ</li><li>Terms Of Services</li></ul></div>
<div class="foot-col contact" style="left:563px"><h4>CONTACT US</h4><ul>
  <li><svg width="12" height="16" viewBox="0 0 12 16"><path d="M6 0a6 6 0 0 0-6 6c0 4 6 10 6 10s6-6 6-10a6 6 0 0 0-6-6zm0 8.5A2.5 2.5 0 1 1 6 3.5a2.5 2.5 0 0 1 0 5z" fill="#fff"/></svg><span>PO Box 4410, Harlbridge,<br>HB2 9LX</span></li>
  <li><svg width="12" height="12" viewBox="0 0 12 12"><path d="M2 0l3 3-1.5 1.5a7 7 0 0 0 4 4L9 7l3 3-2 2C5 12 0 7 0 2z" fill="#fff"/></svg><span>(+44) 0161 555 0148</span></li>
  <li><svg width="13" height="10" viewBox="0 0 13 10"><rect width="13" height="10" fill="#fff"/><polyline points="0,0 6.5,5 13,0" fill="none" stroke="var(--navy)"/></svg><span>info@plinthmoorassessments.example</span></li>
</ul></div>
<div class="foot-col news" style="left:818px"><h4>NEWSLETTER SUBSCRIPTION</h4><p>Register your Email Address to get more Information about us</p><div class="mail">Email Address</div><div class="sub">SUBSCRIBE</div></div>

<div class="abs social"><span></span><span></span><span></span><span></span></div>
<div class="abs copy">Copyrights © 2019 Plinthmoor Assessments. All Rights Reserved &nbsp; | &nbsp; Privacy Policy.</div>

</body>
</html>
```